Vantor Ridge needs a Business Card Design

We need a business card design for an Information Technology company based in Fairfax Virginia called Vantor Ridge. We want the business card to use our logo colors. We need it to be double-sided. The business card needs to look professional but we would like it to be unique. You can get company information from our web site (http://www.vantorridgellc.example).

Target Market(s)

Target market is Government Agencies and Business Professionals.

Industry/Entity Type

Business

Requirements
Must have
• Must have section for company name, company address, company URL, employee name, title, phone and email. Also must have company logo and space for entering logos.

```html
<!DOCTYPE html>
<html lang="en">
<head>
<meta charset="utf-8">
<title>Vantor Ridge – Business Card</title>
<link rel="stylesheet" href="https://fonts.googleapis.com/css2?family=Open+Sans:wght@400;700&family=Oswald:wght@500&display=swap">
<style>
  :root {
    --stage: #e4e8ea;
    --card-white: #ffffff;
    --card-dark: #2a2a2a;
    --brand-blue: #1d5fb4;
    --brand-navy: #1f3a9a;
    --text-grey: #6f6f6f;
    --icon-grey: #8a8a8a;
    --accent-red: #d9343a;
    --faint: #f1f1f1;
  }
  * { box-sizing: border-box; margin: 0; padding: 0; }
  html, body { width: 1200px; height: 960px; overflow: hidden; }
  body {
    background: var(--stage);
    font-family: "Open Sans", Arial, sans-serif;
    position: relative;
  }
  .card {
    position: absolute;
    left: 250px;
    width: 700px;
    height: 400px;
    box-shadow: 0 6px 18px rgba(0,0,0,.18);
    overflow: hidden;
  }
  .card--front { top: 60px; background: var(--card-white); }
  .card--back  { top: 500px; background: var(--card-dark); }

  .brand {
    display: flex;
    align-items: center;
    gap: 12px;
  }
  .brand__mark {
    width: 30px; height: 30px;
    background: var(--brand-navy);
  }
  .brand__name {
    font-weight: 700;
    color: var(--brand-blue);
    font-size: 28px;
    letter-spacing: .5px;
    white-space: nowrap;
  }

  .card--front .brand { position: absolute; top: 38px; right: 40px; }

  .backdrop-pattern {
    position: absolute;
    left: 0; bottom: 0;
    width: 100%; height: 110px;
    background: linear-gradient(180deg, rgba(241,241,241,0) 0%, var(--faint) 100%);
  }

  .identity {
    position: absolute;
    left: 0; top: 188px;
    display: flex;
    align-items: flex-start;
  }
  .identity__bar {
    width: 90px; height: 26px;
    margin-top: 10px;
    background: var(--brand-navy);
  }
  .identity__text { margin-left: 12px; }
  .identity__name { white-space: nowrap; line-height: 1; }
  .identity__first {
    font-family: "Oswald", "Arial Narrow", sans-serif;
    font-weight: 500;
    font-size: 36px;
    color: var(--brand-blue);
    letter-spacing: .5px;
  }
  .identity__last {
    font-size: 30px;
    color: var(--text-grey);
    margin-left: 4px;
  }
  .identity__title {
    display: block;
    text-align: right;
    font-size: 16px;
    color: var(--text-grey);
    margin-top: 4px;
  }

  .contact {
    position: absolute;
    left: 392px; top: 148px;
    padding-left: 16px;
    border-left: 2px solid var(--accent-red);
    list-style: none;
    font-size: 13px;
    color: var(--text-grey);
    line-height: 1.4;
  }
  .contact__item { display: flex; align-items: flex-start; gap: 10px; margin-bottom: 12px; }
  .contact__item:last-child { margin-bottom: 0; }
  .contact__icon { width: 14px; height: 14px; flex: none; margin-top: 2px; fill: var(--icon-grey); }

  .band {
    position: absolute;
    left: 0; top: 125px;
    width: 100%; height: 140px;
    background: var(--card-white);
    display: flex;
    justify-content: center;
    align-items: center;
  }
  .band .brand__mark { width: 52px; height: 52px; }
  .band .brand__name { font-size: 46px; }
</style>
</head>
<body>

  <section class="card card--front" aria-label="Business card front">
    <div class="backdrop-pattern" role="img" aria-label="Faint pattern of small diamond shapes"></div>

    <div class="brand">
      <span class="brand__mark"></span>
      <span class="brand__name">Vantor Ridge</span>
    </div>

    <div class="identity">
      <span class="identity__bar"></span>
      <div class="identity__text">
        <p class="identity__name"><span class="identity__first">EMPLOYEE</span><span class="identity__last">Name</span></p>
        <span class="identity__title">title</span>
      </div>
    </div>

    <ul class="contact">
      <li class="contact__item">
        <svg class="contact__icon" viewBox="0 0 14 14"><circle cx="7" cy="4" r="3.2"/><path d="M1 14c0-3.6 2.7-6 6-6s6 2.4 6 6z"/></svg>
        <span>company address,<br>your detail address</span>
      </li>
      <li class="contact__item">
        <svg class="contact__icon" viewBox="0 0 14 14"><path d="M3 1l2.4 2.6-1.3 1.8c.9 1.9 2.5 3.5 4.4 4.4l1.8-1.3L13 11l-1.6 2C6 13 1 8 1 2.6z"/></svg>
        <span>122233334455</span>
      </li>
      <li class="contact__item">
        <svg class="contact__icon" viewBox="0 0 14 14"><path d="M1 3h12v8H1z M1 3l6 4.5L13 3" fill="var(--icon-grey)"/><path d="M1.5 3.5l5.5 4 5.5-4" stroke="#fff" stroke-width="1" fill="none"/></svg>
        <span>info@email</span>
      </li>
      <li class="contact__item">
        <svg class="contact__icon" viewBox="0 0 14 14"><path d="M3.5 12a3 3 0 0 1-.3-6A4 4 0 0 1 11 5.2 3.4 3.4 0 0 1 10.7 12z"/></svg>
        <span>company URL</span>
      </li>
    </ul>
  </section>

  <section class="card card--back" aria-label="Business card back">
    <div class="band">
      <div class="brand">
        <span class="brand__mark"></span>
        <span class="brand__name">Vantor Ridge</span>
      </div>
    </div>
  </section>

</body>
</html>
```